Make it cool to work near where you are...

Calling all creatives - create the ultimate cool card for people who want to cut their commute.

Here at FarlowBench we've got what can best be described as an Quillet card for desks - and we want to brighten up the wallets of our most loyal users.

So, pitch us your ideas and you might see your design on cards being flashed across the country - and we've thrown in a bit of cash too.

Do see our brief card guidelines - with a couple of past examples thrown in.

```html
<!DOCTYPE html>
<html lang="en">
<head>
<meta charset="utf-8">
<title>FarlowBench – Member Cards</title>
<link rel="stylesheet" href="https://fonts.googleapis.com/css2?family=Arimo:wght@400;700&display=swap">
<style>
  :root {
    --page-bg: #d8d2c8;
    --card-bg: #ffffff;
    --card-edge: #2b2b2b;
    --band: #3a3a3c;
    --brand-pink: #e5197a;
    --ink: #111111;
    --band-text: #f2f2f2;
    --badge-fill: #e4e4e4;
    --badge-rim: #f7f7f7;
  }
  * { box-sizing: border-box; margin: 0; padding: 0; }
  html, body {
    width: 966px;
    height: 1200px;
    overflow: hidden;
    background: var(--page-bg);
    font-family: "Arimo", Arial, sans-serif;
  }
  .sheet {
    position: relative;
    width: 966px;
    height: 1200px;
  }
  .card {
    position: absolute;
    left: 74px;
    width: 814px;
    height: 512px;
    background: var(--card-bg);
    border: 2px solid var(--card-edge);
    border-radius: 40px;
    overflow: hidden;
  }
  .card--front { top: 60px; }
  .card--back { top: 622px; }

  .brand-name {
    position: absolute;
    font-weight: 700;
    font-size: 62px;
    letter-spacing: -1.5px;
    color: var(--brand-pink);
    line-height: 1;
    white-space: nowrap;
  }
  .card--front .brand-name {
    right: 62px;
    top: 146px;
  }
  .card--back .brand-name {
    left: 0;
    right: 0;
    text-align: center;
    top: 138px;
  }

  .phone {
    position: absolute;
    left: 70px;
    top: 286px;
    font-weight: 700;
    font-size: 35px;
    color: var(--ink);
    letter-spacing: 0.3px;
  }

  .footer-band {
    position: absolute;
    left: 0;
    right: 0;
    bottom: 0;
    height: 72px;
    background: var(--band);
  }
  .web-address {
    position: absolute;
    left: 0;
    width: 628px;
    bottom: 20px;
    text-align: center;
    font-size: 24px;
    letter-spacing: 2px;
    color: var(--band-text);
  }

  .badge {
    position: absolute;
    left: 598px;
    bottom: 30px;
    width: 168px;
    height: 110px;
    border-radius: 18px;
    background: var(--badge-fill);
    border: 4px solid var(--badge-rim);
  }
</style>
</head>
<body>
  <main class="sheet">
    <section class="card card--front" aria-label="Card front">
      <p class="brand-name">FarlowBench</p>
      <p class="phone">0019 555 310 642</p>
      <div class="footer-band"></div>
      <p class="web-address">www.farlowbench.com</p>
      <div class="badge" aria-hidden="true"></div>
    </section>

    <section class="card card--back" aria-label="Card back">
      <p class="brand-name">FarlowBench</p>
      <div class="footer-band"></div>
      <p class="web-address">www.farlowbench.com</p>
      <div class="badge" aria-hidden="true"></div>
    </section>
  </main>
</body>
</html>
```